Vellow Table

A quick run down of the iPhone app and what it does:

1. It has a home screen for that restaurant that will guide you to the menu.
2. You can search the menu which has all the pictures of the items on the menu.
3. There are also ratings from the users on each item.
4. You can also order and pay from the app.

Please see this link to look at the wire-frame we have created (Click on the buttons to move from page to page)
https://www.brantoke.com/editor/live/preview/p_9XqLmzRtWpKdhYvBcNsJfa2GE4uoxm3.5820417396621

We would like something that is very clean, minimalist and uses modern design to convey the feeling of cultured.

I would like the designer to create at least 5 pages:

1. The Home screen to the restaurant. (call it Harbor Plateau) You can redo the buttons to make it look better. Like have a logo or something better than box buttons. Please use good looking easy to read fonts, Modern you might say.

2. and 3. The Menu page with 3 items and pictures per menu title like Appetizers and Entrees have it look as if it is dropping down (you can use your own photos or some from the web with descriptions like what you see on the Wire-frame)

4. The item drill down, as you click on an item from the menu it comes up with a larger photo of the item and the description and also the rating under the description. (see wire-frame)

5. The order page with items from the menu on the order page with prices.

I would like for the bottom menu to be updated with some nice looking buttons. For one the help now button I would like to have a circle with an outline of a person raising their hand.

I currently don't have a logo or photos so I will rely on your discretion to find the photos you need. I also have no particular colors in mind but here are some app designs I really like.

http://wovenpixa.com/tagged/app_drelm#show-all

http://48.media.glimrost.com/3a9e61f0c4d2b8e7a15f9c3d08b2e6a4/glimrost_k4trpwqzXB2m83oep2_400.png (put the item name on this and a plus sign in the top right of the photo)

http://52.media.glimrost.com/b7f2a09e3c6d41e85f0a9c27d3e1b6f8/glimrost_k4trv5hyLQ7m83oep2_400.png ( take out all the words and put in all the information I have on the page with the large picture, from my wire-frame, the drill down page)

If you follow the same sort of app design with a photo in the background of the restaurant home page and clear design like this you will for sure win.

Also after this is done I will most likely have the winning designer create my logo, and app icon.

Target Market(s)

The target market of this App are people that can afford to eat out and enjoy using technology to have a better dining experience. Ages 16 to 45 Male and Female.

Industry/Entity Type

Restaurant

Font styles to use
Sans Serif

Requirements
Must have
• Clear, high quality photos, I don't want to see any individual pixels. Please read my outline carefully to understand what this app will do.
Nice to have
• I want to feel like I'm having a good experience from the moment I open the app the the moment I finish my meal with the app. Come up with something simple and creative for the user to experience while dining.
Should not have
• Please do not just submit my wire-frame in different colors that will be a waste of your time and mine. I don't want to see boxes as the buttons.

```html
<!DOCTYPE html>
<html lang="en">
<head>
<meta charset="utf-8">
<title>Vellow Table – Harbor Plateau app screens</title>
<link rel="stylesheet" href="https://fonts.googleapis.com/css2?family=Open+Sans:wght@400;600;700&family=Oswald:wght@400;500&display=swap">
<style>
:root{
  --stage:#d9d9d9;
  --white:#ffffff;
  --header-bg:#f2f2f2;
  --link-blue:#3f86c6;
  --title-blue:#3b7bb4;
  --nav-blue:#4a86bf;
  --nav-dark:#2e3237;
  --caption:rgba(20,22,24,.78);
  --muted:#9a9a9a;
  --text:#333333;
  --rule:#e6e6e6;
  --star:#4a86bf;
  --star-off:#d5dde6;
  --teal:#1db3b3;
  --green:#2bbd21;
  --rating-bg:#fcf1f1;
  --qty-bg:#e8e8e8;
  --submit:#477fb2;
  --waiter:#23384f;
}
*{box-sizing:border-box;margin:0;padding:0}
html,body{width:1200px;height:675px;overflow:hidden;background:var(--stage);font-family:"Open Sans",Arial,sans-serif}
.screen{position:absolute;top:0;height:675px;background:var(--white);overflow:hidden;box-shadow:0 0 8px rgba(0,0,0,.25)}
.screen--menu{left:0;width:394px}
.screen--detail{left:405px;width:391px}
.screen--order{left:805px;width:395px}

/* menu screen */
.topbar{position:absolute;top:0;left:0;right:0;height:59px;background:var(--header-bg);border-bottom:1px solid #cfcfcf;color:var(--link-blue);font-size:16px}
.topbar__back{position:absolute;left:8px;top:20px}
.topbar__title{position:absolute;left:165px;top:20px}
.dish-card{position:absolute;left:0;right:0;overflow:hidden}
.dish-card--party{top:59px;height:278px}
.dish-card--cool{top:337px;height:272px}
.photo{position:absolute;inset:0}
.photo--party{background:radial-gradient(ellipse at 35% 30%,#9aa48f 0%,#3a4036 45%,#141614 100%)}
.photo--party::after{content:"";position:absolute;left:30px;top:95px;width:260px;height:110px;border-radius:50%;background:radial-gradient(ellipse,#c23a2a 0%,#6c8a3a 45%,rgba(0,0,0,0) 75%)}
.photo--melon{background:radial-gradient(ellipse at 45% 45%,#e2403a 0%,#b82a28 40%,#2e4a4a 80%,#1c2b2e 100%)}
.add-btn{position:absolute;right:12px;width:35px;height:35px}
.dish-card__caption{position:absolute;left:0;right:0;bottom:0;background:var(--caption);color:var(--white);padding:0 11px}
.dish-card--party .dish-card__caption{height:71px}
.dish-card--cool .dish-card__caption{height:67px}
.dish-card__name{font-size:21px;font-weight:400;margin-top:18px;line-height:1.1}
.dish-card__tag{font-size:11px;margin-top:3px;padding-left:2px}
.tabbar{position:absolute;left:0;right:0;bottom:0;height:66px;display:flex;justify-content:space-around;align-items:flex-start}
.tabbar--blue{background:var(--nav-blue)}
.tabbar--dark{background:var(--nav-dark)}
.tab{display:flex;flex-direction:column;align-items:center;color:var(--white);font-size:7.5px;font-weight:700;letter-spacing:.2px;padding-top:3px}
.tab svg{width:40px;height:40px}
.tab span{margin-top:5px}
.tabbar--dark .tab{font-size:9.5px;font-weight:600;padding-top:4px}
.tabbar--dark .tab svg{width:48px;height:48px}
.tabbar--dark .tab span{margin-top:2px}
.divider{width:1px;height:50px;background:#454a50;margin-top:8px}

/* detail screen */
.hero{position:absolute;left:0;top:0;width:391px;height:267px}
.hero__caption{position:absolute;left:0;right:0;bottom:0;height:81px;background:var(--caption);color:var(--white);padding:22px 26px 0}
.hero__name{font-size:21px;line-height:1.1}
.hero__tag{font-size:11px;margin-top:4px}
.waiter-btn{position:absolute;right:16px;top:9px;width:42px;height:42px}
.scoreboard{position:absolute;left:0;right:0;top:267px;height:87px;background:var(--rating-bg);border-bottom:1px solid var(--rule)}
.score__label{position:absolute;top:9px;font-size:13px;color:var(--text)}
.score__label--overall{left:50px;color:#a8a8a8}
.score__label--ratings{left:178px}
.score__label--reviews{left:319px}
.stars{position:absolute;display:flex;gap:2px}
.stars svg{width:20px;height:20px}
.scoreboard .stars{left:20px;top:40px}
.scoreboard .stars svg{width:22px;height:22px}
.score__badge{position:absolute;top:31px;width:58px;height:58px;border-radius:50%;color:var(--white);font-family:"Oswald",sans-serif;font-size:25px;display:flex;align-items:center;justify-content:center}
.score__badge--rating{left:170px;background:var(--teal)}
.score__badge--reviews{left:317px;background:var(--green)}
.review{position:absolute;left:0;right:0;padding:0 16px;color:var(--text)}
.review--first{top:384px;height:128px;border-bottom:1px solid var(--rule)}
.review--second{top:524px}
.review__name{position:absolute;left:16px;top:6px;font-size:15px;font-weight:600;color:var(--title-blue)}
.review__rating{position:absolute;right:22px;top:3px;display:flex;align-items:center;gap:6px;font-size:12px}
.review__rating .stars{position:static}
.review__headline{margin-top:29px;text-align:center;font-size:14.5px;line-height:1.2}
.review__body{font-size:13.7px;line-height:1.3;margin-top:1px;padding-left:2px}
.review__body .indent{padding-left:46px}

/* order screen */
.order-item{position:absolute;left:0;right:0;height:70px;border-bottom:1px solid #efefef}
.order-item__name{position:absolute;left:29px;top:12px;font-size:21px;font-weight:700;color:var(--title-blue);line-height:1.1}
.order-item__type{position:absolute;left:31px;top:39px;font-size:10px;color:var(--text)}
.stepper{position:absolute;left:275px;top:11px;width:112px;height:30px}
.stepper__btn{position:absolute;top:1px;width:29px;height:29px}
.stepper__btn--plus{left:0}
.stepper__btn--minus{right:0}
.stepper__qty{position:absolute;left:36px;top:1px;width:40px;height:28px;background:var(--qty-bg);border-radius:4px;text-align:center;font-size:16px;line-height:28px;color:#444}
.stepper__price{position:absolute;left:36px;top:33px;width:40px;text-align:center;font-size:12px;font-weight:600;color:#b8b8b8}
.submit{position:absolute;left:37px;top:535px;width:305px;height:52px;border-radius:4px;background:var(--submit);color:var(--white);font-size:16px;font-weight:700;display:flex;align-items:center;justify-content:center;box-shadow:0 1px 2px rgba(0,0,0,.25)}
</style>
</head>
<body>
<svg width="0" height="0" style="position:absolute">
  <defs>
    <symbol id="star" viewBox="0 0 24 24"><path d="M12 1.5l3.1 7.1 7.6.6-5.8 5 1.8 7.5L12 17.7l-6.7 4 1.8-7.5-5.8-5 7.6-.6z"/></symbol>
    <symbol id="plus-ring" viewBox="0 0 36 36"><circle cx="18" cy="18" r="16.5" fill="none" stroke="currentColor" stroke-width="2"/><path d="M18 10v16M10 18h16" stroke="currentColor" stroke-width="2.6" stroke-linecap="round"/></symbol>
    <symbol id="minus-ring" viewBox="0 0 36 36"><circle cx="18" cy="18" r="16.5" fill="none" stroke="currentColor" stroke-width="2"/><path d="M10 18h16" stroke="currentColor" stroke-width="2.6" stroke-linecap="round"/></symbol>
    <symbol id="hand-raised" viewBox="0 0 40 40"><circle cx="18" cy="13" r="4.2" fill="currentColor"/><path d="M11 33v-9c0-3 2-5 5-5h4l5-5 2-7 2 .6-1.6 8L22 22v11z" fill="currentColor"/><text x="26" y="12" font-size="8" font-family="Open Sans,sans-serif" font-weight="700" fill="currentColor">?</text></symbol>
  </defs>
</svg>

<!-- Screen: menu list -->
<section class="screen screen--menu">
  <header class="topbar"><span class="topbar__back">&lt; Back</span><span class="topbar__title">Appetizers</span></header>

  <article class="dish-card dish-card--party">
    <div class="photo photo--party" role="img" aria-label="Photo of cucumber cups topped with cream and tomato, with vegetable sticks in glasses"></div>
    <svg class="add-btn" style="top:17px;color:#fff"><use href="#plus-ring"/></svg>
    <div class="dish-card__caption"><h2 class="dish-card__name">Easy Party Appetizers</h2><p class="dish-card__tag">Very cool spot with great appetizers!</p></div>
  </article>

  <article class="dish-card dish-card--cool">
    <div class="photo photo--melon" role="img" aria-label="Photo of watermelon bites topped with cream and herbs on a platter"></div>
    <svg class="add-btn" style="top:18px;color:#fff"><use href="#plus-ring"/></svg>
    <div class="dish-card__caption"><h2 class="dish-card__name">Coool Appetizers</h2><p class="dish-card__tag">Very cool spot with great appetizers!</p></div>
  </article>

  <nav class="tabbar tabbar--blue">
    <div class="tab"><svg viewBox="0 0 40 40" fill="none" stroke="#fff" stroke-width="2"><circle cx="20" cy="20" r="18.5"/><rect x="12" y="10" width="13" height="18" fill="#fff" stroke="none"/><path d="M14.5 14h8M14.5 18h8M14.5 22h8" stroke="#4a86bf" stroke-width="1.4"/><path d="M27 12v16" stroke-width="2.4"/></svg><span>ORDER</span></div>
    <div class="tab"><svg viewBox="0 0 40 40" fill="none" stroke="#fff" stroke-width="2"><circle cx="20" cy="20" r="18.5"/><use href="#hand-raised" x="1" y="1" width="38" height="38" color="#fff" stroke="none"/></svg><span>HELP NOW</span></div>
    <div class="tab"><svg viewBox="0 0 40 40" fill="none" stroke="#fff" stroke-width="2"><circle cx="20" cy="20" r="18.5"/><circle cx="20" cy="19" r="6.5"/><path d="M10 9v7c0 2 2 2 2 2v13M12 9v6M14 9v7c0 2-2 2-2 2M28 9c-3 2-3 8 0 10v12" stroke-linecap="round"/></svg><span># TABLE</span></div>
    <div class="tab"><svg viewBox="0 0 40 40" fill="none" stroke="#fff" stroke-width="2"><circle cx="20" cy="20" r="18.5"/><path d="M12 14h16M12 20h16M12 26h16" stroke-width="2.6" stroke-linecap="round"/></svg><span>MENU</span></div>
  </nav>
</section>

<!-- Screen: item detail -->
<section class="screen screen--detail">
  <div class="hero">
    <div class="photo photo--melon" role="img" aria-label="Large photo of watermelon bites topped with cream and herbs"></div>
    <svg class="waiter-btn" viewBox="0 0 42 42"><circle cx="21" cy="21" r="21" fill="#23384f"/><use href="#hand-raised" x="4" y="4" width="34" height="34" color="#fff"/></svg>
    <div class="hero__caption"><h1 class="hero__name">Coool Appetizers</h1><p class="hero__tag">Very cool spot with great appetizers!</p></div>
  </div>

  <div class="scoreboard">
    <span class="score__label score__label--overall">Over all</span>
    <div class="stars">
      <svg fill="var(--star)"><use href="#star"/></svg><svg fill="var(--star)"><use href="#star"/></svg><svg fill="var(--star)"><use href="#star"/></svg><svg fill="var(--star-off)"><use href="#star"/></svg><svg fill="var(--star-off)"><use href="#star"/></svg>
    </div>
    <span class="score__label score__label--ratings">Ratings</span>
    <div class="score__badge score__badge--rating">4.5</div>
    <span class="score__label score__label--reviews">Reviews</span>
    <div class="score__badge score__badge--reviews">243</div>
  </div>

  <article class="review review--first">
    <h3 class="review__name">Owen Carter</h3>
    <div class="review__rating">Rating <div class="stars"><svg fill="var(--star)"><use href="#star"/></svg><svg fill="var(--star)"><use href="#star"/></svg><svg fill="var(--star)"><use href="#star"/></svg><svg fill="var(--star)"><use href="#star"/></svg><svg fill="var(--star)"><use href="#star"/></svg></div></div>
    <p class="review__headline">“Very cool spot with great appetizers!”</p>
    <p class="review__body"><span class="indent">We found this place upon recommendation</span><br>of restaurant close by. We sat at the bar, had a few drinks, some appetizers &amp; enjoyed chatting with the owner. Really enjoyed.</p>
  </article>

  <article class="review review--second">
    <h3 class="review__name">Theo</h3>
    <div class="review__rating">Rating <div class="stars"><svg fill="var(--star)"><use href="#star"/></svg><svg fill="var(--star)"><use href="#star"/></svg><svg fill="var(--star)"><use href="#star"/></svg><svg fill="var(--star)"><use href="#star"/></svg><svg fill="var(--star-off)"><use href="#star"/></svg></div></div>
    <p class="review__headline">“Great evening of wine tasting”</p>
    <p class="review__body">Five friends enjoyed a great evening of wine tasting, we also came back rather late the following evening</p>
  </article>

  <nav class="tabbar tabbar--dark">
    <div class="tab"><svg viewBox="0 0 48 48" fill="none" stroke="#4a86bf" stroke-width="2"><circle cx="24" cy="24" r="22.5"/><use href="#hand-raised" x="5" y="5" width="38" height="38" color="#fff" stroke="none"/></svg><span>Help Now</span></div>
    <div class="divider"></div>
    <div class="tab"><svg viewBox="0 0 48 48" fill="none" stroke="#4a86bf" stroke-width="2"><circle cx="24" cy="24" r="22.5"/><path d="M13 30a11 11 0 0 1 22 0z" fill="#fff" stroke="none"/><path d="M11 32h26" stroke="#fff" stroke-width="2.6"/><circle cx="24" cy="17" r="1.8" fill="#fff" stroke="none"/></svg><span>Order</span></div>
  </nav>
</section>

<!-- Screen: order summary -->
<section class="screen screen--order">
  <div class="order-item" style="top:5px">
    <h3 class="order-item__name">Cool Appetizers</h3><span class="order-item__type">APPETIZER</span>
    <div class="stepper"><svg class="stepper__btn stepper__btn--plus" style="color:#444"><use href="#plus-ring"/></svg><span class="stepper__qty">2</span><svg class="stepper__btn stepper__btn--minus" style="color:#444"><use href="#minus-ring"/></svg><span class="stepper__price">$10</span></div>
  </div>
  <div class="order-item" style="top:75px">
    <h3 class="order-item__name">Red Fizz</h3><span class="order-item__type">CHIPS</span>
    <div class="stepper"><svg class="stepper__btn stepper__btn--plus" style="color:#444"><use href="#plus-ring"/></svg><span class="stepper__qty">2</span><svg class="stepper__btn stepper__btn--minus" style="color:#444"><use href="#minus-ring"/></svg><span class="stepper__price">$5</span></div>
  </div>
  <div class="order-item" style="top:145px">
    <h3 class="order-item__name">Lime Spark</h3><span class="order-item__type">COOL DRINKS</span>
    <div class="stepper"><svg class="stepper__btn stepper__btn--plus" style="color:#444"><use href="#plus-ring"/></svg><span class="stepper__qty">1</span><svg class="stepper__btn stepper__btn--minus" style="color:#444"><use href="#minus-ring"/></svg><span class="stepper__price">$3</span></div>
  </div>
  <div class="order-item" style="top:215px">
    <h3 class="order-item__name">Cheese Burger</h3><span class="order-item__type">ENTREES</span>
    <div class="stepper"><svg class="stepper__btn stepper__btn--plus" style="color:#444"><use href="#plus-ring"/></svg><span class="stepper__qty">1</span><svg class="stepper__btn stepper__btn--minus" style="color:#444"><use href="#minus-ring"/></svg><span class="stepper__price">$5</span></div>
  </div>

  <div class="submit">Submit Order</div>

  <nav class="tabbar tabbar--dark">
    <div class="tab"><svg viewBox="0 0 48 48" fill="none" stroke="#4a86bf" stroke-width="2"><circle cx="24" cy="24" r="22.5"/><path d="M15 33l2-7 14-14 5 5-14 14z" fill="#fff" stroke="none"/><path d="M29 14l5 5" stroke="#2e3237" stroke-width="1.5"/></svg><span>Review</span></div>
    <div class="divider"></div>
    <div class="tab"><svg viewBox="0 0 48 48" fill="none" stroke="#4a86bf" stroke-width="2"><circle cx="24" cy="24" r="22.5"/><circle cx="20" cy="16" r="3.2" fill="#fff" stroke="none"/><path d="M15 34v-9c0-3 2-4 4-4h3l3 3 5-6 2 1-6 9h-3v6z" fill="#fff" stroke="none"/><path d="M29 12l5-2-1 5z" fill="#fff" stroke="none"/></svg><span>Note for Waiter</span></div>
    <div class="divider"></div>
    <div class="tab"><svg viewBox="0 0 48 48" fill="none" stroke="#4a86bf" stroke-width="2"><circle cx="24" cy="24" r="22.5"/><text x="24" y="33" text-anchor="middle" font-family="Open Sans,sans-serif" font-weight="700" font-size="24" fill="#fff" stroke="none">$</text></svg><span>Pay Now</span></div>
  </nav>
</section>
</body>
</html>
```